Signage Design Project - Florida Vacation Resort Monument Sign

I need a design for the main identification sign outside of a resort in Florida. This is a sign that will be located at ground level near the entrance to the resort.

Text to include:

"4818" (This is the property address numbers, no street name necessary)

"Coral Haven" (This is the name of the resort)

"Heated Pool" (bullet point)
"Tiki Hut" (bullet point)
"Beach Access" (bullet point)

"Weekly/Monthly Rentals" (text to appear at bottom of sign)

Dimensions: 55.5"wide x 43.5"tall

Some design elements can protrude from the dimensions, as long as they are not too thin. It will ultimately need to be cut out of wood and if a design element is thin and sticks out of the box, it will be likely to break off.

***The artwork must be vectored.***

Please use whatever design elements you'd like in full color. A palm tree might make sense because of the name "Coral Haven", but I don't want to limit your creativity!

The website is here: http://www.coral-haven-example.com

They have a tour your can click on at the bottom for more pictures to get a feel for the property.

```html
<!DOCTYPE html>
<html lang="en">
<head>
<meta charset="utf-8">
<title>Coral Haven Resort – Monument Sign</title>
<link rel="stylesheet" href="https://fonts.googleapis.com/css2?family=Cormorant+Garamond:wght@500;600&family=Playfair+Display:ital,wght@1,400&family=Montserrat:wght@400&display=swap">
<style>
  :root {
    --sand: #dda874;
    --forest: #0e5a3e;
    --gold: #f8b816;
    --ink: #111111;
    --cream: #f1f0ec;
  }
  html, body {
    margin: 0;
    padding: 0;
    overflow: hidden;
    background: var(--sand);
  }
  .sign {
    position: relative;
    width: 1200px;
    height: 941px;
    background: var(--sand);
    overflow: hidden;
  }
  .address-number {
    position: absolute;
    top: 0;
    right: 42px;
    margin: 0;
    font-family: "Montserrat", sans-serif;
    font-weight: 400;
    font-size: 110px;
    letter-spacing: 3px;
    color: var(--forest);
  }
  .emblem {
    position: absolute;
    left: 0;
    top: 0;
    width: 1200px;
    height: 941px;
  }
  .emblem-rim { fill: var(--gold); }
  .emblem-field { fill: var(--forest); }
  .resort-name {
    position: absolute;
    top: 239px;
    left: 0;
    width: 100%;
    margin: 0;
    text-align: center;
    font-family: "Cormorant Garamond", serif;
    font-weight: 500;
    color: var(--cream);
    line-height: 1;
  }
  .resort-name .name-main {
    display: block;
    font-size: 90px;
    letter-spacing: 4px;
    text-transform: uppercase;
  }
  .resort-name .name-sub {
    display: block;
    margin-top: 2px;
    font-size: 60px;
    letter-spacing: 4px;
    text-transform: uppercase;
  }
  .amenities {
    position: absolute;
    top: 510px;
    left: 0;
    width: 100%;
    margin: 0;
    padding: 0;
    list-style: none;
    text-align: center;
    font-family: "Playfair Display", serif;
    font-style: italic;
    font-size: 78px;
    line-height: 86px;
    letter-spacing: 2px;
    color: var(--ink);
  }
  .rentals-band {
    position: absolute;
    left: 0;
    bottom: 0;
    width: 100%;
    height: 121px;
    background: var(--forest);
    display: flex;
    align-items: center;
    justify-content: center;
  }
  .rentals-band p {
    margin: 0;
    font-family: "Cormorant Garamond", serif;
    font-weight: 500;
    font-size: 78px;
    letter-spacing: 3px;
    color: var(--cream);
  }
</style>
</head>
<body>
  <main class="sign">
    <p class="address-number">4818</p>
    <svg class="emblem" viewBox="0 0 1200 941" aria-hidden="true">
      <ellipse class="emblem-rim" cx="609" cy="296" rx="434" ry="192"/>
      <ellipse class="emblem-field" cx="609" cy="296" rx="422" ry="180"/>
    </svg>
    <h1 class="resort-name">
      <span class="name-main">Coral Haven</span>
      <span class="name-sub">Resort</span>
    </h1>
    <ul class="amenities">
      <li>Heated Pool</li>
      <li>Tiki Hut</li>
      <li>Beach Access</li>
    </ul>
    <footer class="rentals-band">
      <p>Weekly/Monthly Rentals</p>
    </footer>
  </main>
</body>
</html>
```